Beauty Salon Industry - Web Design Project

zTrellis is a well-funded start up developing an Online Marketing Platform for small businesses in Europe.
We require a large number of high quality business web designs for our business website builder. Our business websites are seamlessly integrated into our Online Marketing systems and therefore it is important for designers to comply with our Design Guidelines.
This is our second contest and it will focus on the beauty salon industry. We will be running contents every 2-3 weeks for a new industry. Last month, we ran a contest for Builder website designs with 3 top prizes (plus £10 per variation) and we also paid out £25 per design for 20+ entries from designers who did not win the top prizes. So we encourage all entries!
We have included a wire frame this time to encourage you to be as creative as possible with your designs and layout while respecting the following guidelines:
1) You CAN change the layout as much as you like. If you think a vertical menu would look better, then use it. If you think the design would benefit from moving an element to a different location, then you can do that too.
2) You must include ALL the elements in the wire frame in your design.(e.g. latest 2 news entries, a testimonial, 1 gallery image, carousel etc...). Please make sure you have looked through the wire frame and know what is required. Entries that do not include all the elements will not qualify to win.
3) So remember, you CAN change the layout as much as you like but DO NOT remove any elements nor move them to a different page.
4) You may change the size and style of the carousel image. We would like to see as many variations of this as possible.
We are rewarding 3 prizes, and would like the winning designer to design the internal pages to the new design.
As always, if we think your designs could be incorporated into our system, but you do not win the competition, we will reward £25. Therefore, we encourage designers to submit as many designs as possible as we may award up to 25 designs.
Judging criteria : -
1) Visual Design
2) Layout must adhere to best practices and wireframe. If you decide to move elements around significantly please provide reason
3) Functional, informative and drives calls to action
Updates
As usual:
1st place = £350
2nd place = £250
3rd place = £150
Good luck!
Very happy with all the designs submitted so far, and will provide feedback ASAP.
We would like to see you try arranging the elements differently. So please try different navigation types and layouts.
Thanks
Morris
Prize funds for 1st place has been slightly increased.
Thanks
Morris
We have already had some amazing designs submitted. Thanks.
Remember to play with the layout of the elements and try designs with a carousel/slider that is in portrait not just in landscape.
Thanks everyone!
Morris
Hi everyone, we are really enjoying looking through the designs.
We have one NEW requirement. If you have used an image from http://www.quarnex-demo.net/ in your design, could you please replace it with another.
We are not associated with them.
Thank you.
I have just sent a poll around the office to vote on all the designs and hope to have the results soon.
Good luck and I hope to see all your great designs for our next project in a couple of weeks.
Morris
Hi everyone, we hope you have had a good holiday season. We will be rewarding the prizes very soon, hopefully today or tomorrow.
Thanks
Morris
We are currently going through all the designs that did not win our competition and will be contacting the designers of the designs we would like to use in our system, so please keep an eye on your inbox over the next few days.
Thank you
Morris
Target Market(s)
Beauty Salon Industry
Industry/Entity Type
Beauty Salon
Look and feel
Each slider illustrates characteristics of the customer's brand and the style your logo design should communicate.

```html
<!DOCTYPE html>
<html lang="en">
<head>
<meta charset="utf-8">
<title>Lumen Salon</title>
<link href="https://fonts.googleapis.com/css2?family=PT+Sans:ital,wght@0,400;0,700;1,400&display=swap" rel="stylesheet">
<style>
:root{
  --purple:#9b3fa6;
  --purple-light:#c070c9;
  --purple-dark:#6e2477;
  --pink:#e58aee;
  --ink:#222;
  --grey:#888;
  --page:#efefef;
  --panel:#fff;
  --line:#cfcfcf;
  --black:#000;
}
*{box-sizing:border-box;margin:0;padding:0}
html,body{width:1200px;height:1113px;overflow:hidden}
body{position:relative;background:var(--page);font-family:"PT Sans",Arial,sans-serif;color:var(--ink)}
.abs{position:absolute}
.top-rule{left:0;top:0;width:1200px;height:4px;background:var(--purple)}
.header{left:0;top:4px;width:1200px;height:77px;background:var(--black)}
.navband{left:0;top:81px;width:1200px;height:46px;background:linear-gradient(#3a3a3a,#161616);border-top:1px solid #555}
.book-tab{left:891px;top:4px;width:178px;height:25px;background:var(--purple);border-radius:0 0 6px 6px;color:#fff;font-size:13px;text-align:center;line-height:25px;border:1px solid var(--purple-light);border-top:0}
.brand{left:113px;top:6px;display:flex;align-items:center;gap:10px}
.brand-dot{width:116px;height:116px;border-radius:50%;background:#2a2a2a;border:3px solid #777}
.brand-name{color:#fff;font-size:34px;font-weight:400;margin-top:-34px}
.nav{left:406px;top:90px;font-size:18px;color:#fff}
.nav a{color:#fff;text-decoration:none;position:absolute;white-space:nowrap}
.nav a.active{color:var(--pink)}
.slider{left:120px;top:138px;width:637px;height:433px;background:var(--panel);border:1px solid var(--line);box-shadow:0 6px 8px rgba(0,0,0,.18)}
.slide-img{left:10px;top:10px;width:617px;height:412px;background:linear-gradient(120deg,#5a3bd0 0%,#c03ea8 30%,#1a2a5a 55%,#0b1b2b 80%,#1d8fb8 100%)}
.caption{left:10px;top:360px;width:440px;height:62px;background:rgba(20,20,20,.75);color:#fff;padding:4px 0 0 21px}
.caption h2{font-family:Arial,sans-serif;font-weight:400;font-size:24px}
.caption p{font-family:Arial,sans-serif;font-size:16px;margin-top:2px}
.pager{left:450px;top:398px;width:186px;height:24px;background:linear-gradient(90deg,#555,#111);clip-path:polygon(8% 0,100% 0,100% 100%,0 100%);color:#fff;font-size:17px;text-align:right;padding-right:70px;line-height:24px;letter-spacing:2px}
.pager b{color:var(--pink);font-weight:400}
.slide-arrow{top:186px;z-index:2}
.gift{left:769px;top:138px;width:312px;height:182px;background:linear-gradient(#fff,#f1f1f1);border:1px solid var(--line);overflow:hidden}
.gift-tri{left:0;top:0}
.price{right:12px;top:4px;color:#fff;font-size:56px}
.gift-img{left:6px;top:30px;width:97px;height:117px;background:linear-gradient(#3fa8e8,#1561b8);border-radius:6px}
.gift-text{left:121px;top:80px;font-size:18px;line-height:20px;color:#333}
.btn-book{left:41px;top:151px;width:230px;height:30px;background:linear-gradient(var(--purple-light),var(--purple-dark));color:#fff;font-size:17px;text-align:center;line-height:30px;white-space:nowrap}
.panel{background:var(--panel);border:1px solid var(--line);border-radius:3px;overflow:hidden}
.panel-head{height:30px;background:linear-gradient(var(--purple-light),var(--purple));color:#fff;font-size:15px;padding:5px 11px;border-bottom:2px solid #222;white-space:nowrap;letter-spacing:-.2px}
.skills{left:769px;top:331px;width:312px;height:241px}
.skills-img{left:11px;top:45px;width:101px;height:112px;background:linear-gradient(135deg,#1aa79a,#6a2fa8,#e03b7a);border:2px solid #bbb}
.skills p{position:absolute;left:11px;top:40px;width:292px;font-size:12px;line-height:20px;color:#111}
.skills .float{float:left;width:108px;height:118px}
.more{color:var(--purple);font-style:italic;font-size:12px;position:absolute;right:10px;white-space:nowrap}
.logos{left:121px;top:583px;width:960px;height:93px;background:#f7f7f7;border:1px solid #ddd}
.logo-shape{position:absolute;background:#b8b8b8}
.big-head{height:32px;font-size:21px;padding:3px 15px;border-bottom:3px solid #222;letter-spacing:0}
.news{left:119px;top:685px;width:637px;height:181px;border:1px solid var(--purple)}
.news-card{position:absolute;top:32px;height:148px;width:311px;border-right:1px solid var(--purple)}
.news-card+.news-card{border-left:1px solid var(--purple);border-right:0}
.news-img{left:4px;top:13px;width:100px;height:113px;border:2px solid #bbb}
.news-card h3{position:absolute;left:110px;top:10px;font-weight:400;font-size:18px;letter-spacing:-.3px;white-space:nowrap}
.news-card time{position:absolute;left:112px;top:35px;font-style:italic;font-size:12px;color:var(--grey)}
.news-card p{position:absolute;left:110px;top:52px;width:195px;font-size:12.5px;line-height:20px}
.hours{left:769px;top:685px;width:312px;height:181px;border:1px solid var(--purple)}
.hours table{position:absolute;left:14px;top:41px;font-family:Arial,sans-serif;font-size:13px;border-collapse:collapse}
.hours td{height:18px;padding:0}
.hours td:first-child{font-weight:700;width:88px}
.hours td:last-child{width:70px;text-align:center}
.divider{left:177px;top:52px;height:112px;border-left:1px dashed #888}
.address{left:186px;top:42px;width:120px;font-family:Arial,sans-serif}
.address h4{text-align:center;font-size:13px;letter-spacing:1px}
.address p{color:var(--purple);font-style:italic;font-size:13.5px;margin-top:17px;line-height:17px;letter-spacing:.3px;white-space:nowrap}
.address .tel{font-size:14.5px;font-weight:700;margin-top:6px;letter-spacing:.6px}
.testi-band{left:0;top:876px;width:1200px;height:169px;background:#f6f6f6}
.testi-title{left:119px;top:890px;font-size:18px;color:#333;font-weight:400}
.quote{left:120px;top:924px;width:470px;font-style:italic;font-size:12.5px;line-height:20px;color:var(--grey)}
.quote cite{color:#444;margin-left:18px}
.btn-more{left:120px;top:996px;width:70px;height:32px;border:1px solid #999;border-radius:4px;background:linear-gradient(#fff,#e4e4e4);font-size:13px;text-align:center;line-height:30px}
.thumb{top:888px;width:149px;height:143px;border:3px solid #c8c8c8}
.arrow{width:28px;height:28px;border-radius:50%;background:linear-gradient(#fff,#ccc);border:1px solid #888}
.footer{left:0;top:1045px;width:1200px;height:68px;background:linear-gradient(#2a2a2a,#111);border-top:4px solid #999}
.copy{left:119px;top:1073px;color:#fff;font-size:13px}
.foot-nav a{position:absolute;top:1073px;color:#fff;font-size:13px;text-decoration:none}
</style>
</head>
<body>
<div class="abs top-rule"></div>
<header class="abs header"></header>
<div class="abs navband"></div>
<div class="abs book-tab">BOOK NOW- 020 7946 0182</div>
<div class="abs brand"><span class="brand-dot"></span><span class="brand-name">Lumen Salon</span></div>
<nav class="abs nav">
  <a class="active" style="left:0">Home</a><a style="left:84px">Services</a><a style="left:178px">Gallery</a><a style="left:269px">Testimonials</a><a style="left:402px">News</a><a style="left:481px">About Us</a><a style="left:588px">Contact Us</a>
</nav>

<section class="abs slider">
  <div class="abs slide-img" role="img" aria-label="Salon campaign photo with headline artwork"></div>
  <div class="abs caption"><h2>Magnust Ipsum Illicit</h2><p>Habitante Turpis Morbi Egestas Orci Senectus Nibh Et</p></div>
  <div class="abs pager">12<b>3</b>45</div>
  <svg class="abs slide-arrow" style="left:8px" width="22" height="38"><path d="M0 0a19 19 0 0 1 0 38z" fill="#fff"/><path d="M14 11l-10 8 10 8z" fill="#000"/></svg>
  <svg class="abs slide-arrow" style="left:607px" width="22" height="38"><path d="M22 0a19 19 0 0 0 0 38z" fill="#fff"/><path d="M8 11l10 8-10 8z" fill="#000"/></svg>
</section>

<aside class="abs gift">
  <svg class="abs gift-tri" width="312" height="100"><defs><linearGradient id="gp" x1="0" x2="1"><stop offset="0" stop-color="#c070c9"/><stop offset="1" stop-color="#8a2f95"/></linearGradient></defs><path d="M0 0H312V98Z" fill="url(#gp)"/></svg>
  <div class="abs price">$25</div>
  <div class="abs gift-img" role="img" aria-label="Wrapped gift box with red ribbon"></div>
  <div class="abs gift-text">Complimentary<br>gift for first-time<br>clients !</div>
  <div class="abs btn-book">BOOK APPOINTMENT NOW</div>
</aside>

<section class="abs panel skills">
  <div class="panel-head">Let Our Hair &amp; Beauty Skills Blow You Away</div>
  <div class="abs skills-img" role="img" aria-label="Styled hair model portrait"></div>
  <p><span class="float"></span>Pellentesque habitant morbi tristique senectus et netus et malesuada fames ac turpis egestas. Nam id lacus dui, in aliquet orci. Pellentesque habitant morbi tristique senectus et netus et malesuada fames ac turpis egestas. Nam id lacus dui, in aliquet orci. Pellentesque habitant morbi tristique senectus et .</p>
  <span class="more" style="top:215px">&gt;&gt; Read More</span>
</section>

<section class="abs logos" aria-label="Partner brands">
  <span class="logo-shape" style="left:52px;top:30px;width:165px;height:32px;border-radius:4px"></span>
  <span class="logo-shape" style="left:305px;top:8px;width:130px;height:76px;border-radius:4px"></span>
  <span class="logo-shape" style="left:545px;top:10px;width:112px;height:74px;border-radius:4px"></span>
  <span class="logo-shape" style="left:736px;top:6px;width:150px;height:82px;border-radius:4px"></span>
</section>

<section class="abs panel news">
  <div class="panel-head big-head">Latest News</div>
  <article class="news-card" style="left:0">
    <div class="abs news-img" style="background:linear-gradient(#8fd8ec,#2fa3c8)" role="img" aria-label="Christmas snow globe illustration"></div>
    <h3>Book Now For Christmas</h3><time>01-Dec-2011, 12:20 PM</time>
    <p>Our salon is usually very busy for the two weeks before Christmas, so please book early. Call 020 7946 0182 or Contact us.</p>
    <span class="more" style="top:128px;right:14px">&gt;&gt; Read More</span>
  </article>
  <article class="news-card" style="left:324px">
    <div class="abs news-img" style="left:8px;background:linear-gradient(135deg,#1aa79a,#6a2fa8,#e03b7a)" role="img" aria-label="Hair model portrait"></div>
    <h3 style="left:114px">Want to be a Hair Model?</h3><time style="left:116px">01-Dec-2011, 12:30 PM</time>
    <p style="left:114px">We always need models for our portfolio. If you want to become one than contact us.</p>
    <span class="more" style="top:128px">&gt;&gt; Read More</span>
  </article>
</section>

<section class="abs panel hours">
  <div class="panel-head big-head">Our Hours of Operation</div>
  <table>
    <tr><td>Monday</td><td>8:30 - 5:30</td></tr>
    <tr><td>Tuesday</td><td>8:30 - 6:00</td></tr>
    <tr><td>Wednesday</td><td>8:30 - 6:00</td></tr>
    <tr><td>Thursday</td><td>8:30 - 6:00</td></tr>
    <tr><td>Friday</td><td>8:30 - 6:00</td></tr>
    <tr><td>Saturday</td><td>7:00 - 1:00</td></tr>
    <tr><td>Sunday</td><td>Closed</td></tr>
  </table>
  <div class="abs divider"></div>
  <div class="abs address"><h4>Address</h4><p>12 Marlow Lane<br>London, State</p><p class="tel">020 7946 0182</p></div>
  <span class="more" style="top:159px;right:16px">&gt;&gt; View Map</span>
</section>

<div class="abs testi-band"></div>
<h2 class="abs testi-title">Testimonials.</h2>
<blockquote class="abs quote">“Pellentesque habitant morbi tristique senectus et netus et malesuada fames ac turpis egestas. Nam id lacus dui, in aliquet orci. Pellentesque habitant morbi tristique senectus et netus et malesuada fames ac turpis egestas.”<cite>By- Nadia Brennan</cite></blockquote>
<div class="abs btn-more">Read More</div>
<div class="abs thumb" style="left:617px;background:linear-gradient(135deg,#1aa79a,#5a2f98,#e03b7a)" role="img" aria-label="Gallery: teal-lit hair model"></div>
<div class="abs thumb" style="left:772px;background:linear-gradient(135deg,#2a3fd0,#2ab0c8,#b03a8a)" role="img" aria-label="Gallery: curly colourful hairstyle"></div>
<div class="abs thumb" style="left:928px;background:linear-gradient(135deg,#3a2fc0,#d23f9a,#f07ab8)" role="img" aria-label="Gallery: pink wavy hairstyle"></div>
<svg class="abs arrow" style="left:606px;top:948px" viewBox="0 0 28 28"><path d="M17 8l-8 6 8 6z" fill="#333"/></svg>
<svg class="abs arrow" style="left:1058px;top:948px" viewBox="0 0 28 28"><path d="M11 8l8 6-8 6z" fill="#333"/></svg>

<footer class="abs footer"></footer>
<div class="abs copy">© 2011 All Rights Reserved</div>
<nav class="foot-nav">
  <a style="left:636px;text-decoration:underline">Home</a><a style="left:697px">Services</a><a style="left:765px">Gallery</a><a style="left:830px">Testimonials</a><a style="left:926px">About Us</a><a style="left:1004px">Contact Us</a>
</nav>
</body>
</html>
```